Brindle Advisory Business Card Design

Business card for business consulting company, using attached logo. We do financial and strategic consulting, and want a clean, professional image with a bit of fun. Our logo is a flat whale tail, which symbolizes the Orca whale, a highly collaborative, group based animal that is very successful in navigating the ocean, protecting the herd, and hunting. We like the logo that is blue and gray on white one one side, but would be open to a blue card with white lettering on the other side... or whatever you'd suggest
Updates
Hi all - I have had the logo modified to take the shadowing off the tail. I will post it on the brief... under a file name called updated logo. thank you Added Saturday, April 25, 2015
Target Market(s)
Small to medium sized businesses ($10M to $500M in revenue per year), financial and sales executives, general managers, attorneys and CPAs
Industry/Entity Type
Financial
Contact Information for Business Card
Want company name, contact info - name, title, telephone, email, website, linkedin, twitter and Facebook. No physical address yet.
Requirements
Must have
- contemporary design, bold, strong, confident but with a bit of fun. prominently feature the logo and the whale tail icon
Nice to have
- unique touches that would differentiate us from a regular card... for example, logo and writing all on front on white background, but on back - logo in white on a blue background
- open to idea of different shapes of card than standard... but not sure
Should not have
- ?

```html
<!DOCTYPE html>
<html lang="en">
<head>
<meta charset="utf-8">
<title>Brindle Advisory Business Card</title>
<link rel="stylesheet" href="https://fonts.googleapis.com/css2?family=Open+Sans:wght@300;400;600&display=swap">
<style>
  :root {
    --navy: #173d70;
    --navy-deep: #12335f;
    --navy-light: #1f538f;
    --tile: #1b3a63;
    --white: #ffffff;
    --paper: #e9eaec;
    --grey: #8a8f96;
    --text-dark: #173d70;
  }
  * { box-sizing: border-box; margin: 0; padding: 0; }
  html, body { width: 1200px; height: 902px; overflow: hidden; }
  body {
    background: var(--paper);
    font-family: "Open Sans", Arial, sans-serif;
    position: relative;
  }
  .card {
    position: absolute;
    top: 296px;
    width: 540px;
    height: 310px;
    border-radius: 26px;
    overflow: hidden;
    box-shadow: 0 6px 18px rgba(0,0,0,0.18);
  }
  /* Back side */
  .card-back {
    left: 40px;
    background: linear-gradient(135deg, var(--navy-deep) 0%, var(--navy-light) 55%, var(--navy-deep) 100%);
    display: flex;
    flex-direction: column;
    align-items: center;
    justify-content: center;
    gap: 18px;
  }
  .back-tile {
    width: 120px;
    height: 120px;
    border-radius: 20px;
    background: var(--tile);
  }
  .back-name {
    color: var(--white);
    font-weight: 600;
    font-size: 22px;
    letter-spacing: 0.5px;
  }
  /* Front side */
  .card-front {
    left: 620px;
    background: var(--white);
  }
  .contact-panel {
    position: absolute;
    left: 262px;
    top: 0;
    width: 248px;
    height: 100%;
    background: linear-gradient(180deg, var(--navy-light) 0%, var(--navy) 40%, var(--navy-deep) 100%);
    color: var(--white);
    padding: 34px 0 0 30px;
  }
  .contact-panel::before {
    content: "";
    position: absolute;
    left: -11px;
    top: 44px;
    border-top: 11px solid transparent;
    border-bottom: 11px solid transparent;
    border-right: 11px solid var(--navy);
  }
  .person-name {
    font-size: 21px;
    font-weight: 400;
    letter-spacing: 0.3px;
    line-height: 1.1;
  }
  .person-title {
    font-size: 12px;
    font-weight: 300;
    margin-bottom: 22px;
  }
  .contact-list { list-style: none; }
  .contact-list li {
    display: flex;
    align-items: center;
    gap: 10px;
    font-size: 12.5px;
    font-weight: 300;
    height: 22px;
  }
  .contact-list svg { width: 12px; height: 12px; flex: none; }
  .social-mark {
    width: 12px;
    height: 12px;
    background: var(--white);
    border-radius: 2px;
    flex: none;
  }
  .brand {
    position: absolute;
    left: 26px;
    bottom: 34px;
    display: flex;
    align-items: center;
    gap: 10px;
  }
  .brand-square {
    width: 38px;
    height: 38px;
    border-radius: 6px;
    background: var(--navy);
  }
  .brand-name {
    color: var(--text-dark);
    font-size: 22px;
    font-weight: 600;
    line-height: 1;
  }
  .brand-tagline {
    color: var(--grey);
    font-size: 10px;
    font-weight: 400;
    margin-top: 3px;
    text-align: right;
  }
</style>
</head>
<body>

<section class="card card-back" aria-label="Card back">
  <div class="back-tile"></div>
  <div class="back-name">Brindle Advisory</div>
</section>

<section class="card card-front" aria-label="Card front">
  <div class="brand">
    <div class="brand-square"></div>
    <div>
      <div class="brand-name">Brindle Advisory</div>
      <div class="brand-tagline">business consulting</div>
    </div>
  </div>

  <div class="contact-panel">
    <div class="person-name">YOUR NAME</div>
    <div class="person-title">Title</div>
    <ul class="contact-list">
      <li>
        <svg viewBox="0 0 12 12" aria-hidden="true"><path d="M2.5 1 L4.5 1 L5.2 3.6 L4 4.6 C4.7 6 6 7.3 7.4 8 L8.4 6.8 L11 7.5 L11 9.5 C11 10.3 10.3 11 9.5 11 C5 11 1 7 1 2.5 C1 1.7 1.7 1 2.5 1 Z" fill="#fff"/></svg>
        555-014-2290
      </li>
      <li>
        <svg viewBox="0 0 12 12" aria-hidden="true"><rect x="1" y="2.5" width="10" height="7" fill="#fff"/><path d="M1 2.5 L6 6.5 L11 2.5" stroke="#173d70" stroke-width="1" fill="none"/></svg>
        info@brindleadvisory.com
      </li>
      <li>
        <svg viewBox="0 0 12 12" aria-hidden="true"><circle cx="6" cy="6" r="5" fill="none" stroke="#fff" stroke-width="1.2"/><ellipse cx="6" cy="6" rx="2.2" ry="5" fill="none" stroke="#fff" stroke-width="1"/><line x1="1" y1="6" x2="11" y2="6" stroke="#fff" stroke-width="1"/></svg>
        www.brindleadvisory.com
      </li>
      <li><span class="social-mark"></span>/brindleadvisory</li>
      <li><span class="social-mark"></span>@brindleadvisory</li>
      <li><span class="social-mark"></span>/brindleadvisory</li>
    </ul>
  </div>
</section>

</body>
</html>
```